Outdoor mass notification company needing business card design.

Our company name is Harborline Signal Systems Inc located in Amory Mississippi and we sell and maintain "Corvath" Mass Notification Sirens in the US. Outdoor sirens notify people of certain severe dangers such as tornados, severe thunderstorms, flooding, hurricanes and tsunamis. We also serve the oil and gas refining industries to warn of Chemical releases, fires, and lightning alerts.

Contact Information for Business Card

Name, title, cell number, email address

Requirements
Nice to have
• The Corvath logo and also the Tallbrook logo.

```html
<!DOCTYPE html>
<html lang="en">
<head>
<meta charset="utf-8">
<title>Harborline Signal Systems – Business Card</title>
<link href="https://fonts.googleapis.com/css2?family=Libre+Baskerville:wght@700&family=Roboto:wght@400;700&display=swap" rel="stylesheet">
<style>
  :root {
    --backdrop: #3b3537;
    --card-white: #ffffff;
    --card-grey: #7b7b7b;
    --navy: #2f4b66;
    --ink: #1f1f1f;
    --muted: #6d6d6d;
    --rule: #2a2a2a;
    --siren-dark: #3c3c3c;
    --siren-light: #c9c9c9;
    --on-grey: #ffffff;
  }
  * { box-sizing: border-box; margin: 0; padding: 0; }
  html, body {
    width: 1200px; height: 960px; overflow: hidden;
    background: var(--backdrop);
    font-family: "Roboto", Arial, sans-serif;
  }
  .sheet {
    width: 1200px; height: 960px;
    display: flex; flex-direction: column; align-items: center; justify-content: center;
    gap: 50px;
  }
  .card {
    width: 700px; height: 400px; border-radius: 30px;
    position: relative; overflow: hidden;
  }

  /* Back side */
  .card-back { background: var(--card-grey); color: var(--on-grey); }
  .siren {
    position: absolute; border-radius: 6px;
  }
  .siren-column { left: 50px; top: 40px; width: 70px; height: 190px;
    background: linear-gradient(180deg, var(--siren-dark), #5a5a5a); }
  .siren-horn { right: 40px; top: 30px; width: 180px; height: 120px;
    background: linear-gradient(135deg, #e0e0e0, var(--siren-light)); }
  .back-copy {
    position: absolute; left: 0; right: 0; top: 150px; text-align: center;
  }
  .back-title {
    font-family: "Libre Baskerville", Georgia, serif; font-weight: 700;
    font-size: 20px; margin-bottom: 14px;
  }
  .back-lead { font-size: 20px; margin-bottom: 4px; }
  .back-list { font-size: 15px; margin-bottom: 16px; }

  /* Front side */
  .card-front { background: var(--card-white); }
  .brand {
    position: absolute; right: 40px; top: 70px; text-align: right;
    font-family: "Libre Baskerville", Georgia, serif; font-weight: 700;
    color: var(--navy); text-transform: uppercase; line-height: 1.05;
  }
  .brand-line-1 { font-size: 34px; }
  .brand-line-2 { font-size: 24px; letter-spacing: 1px; }
  .person { position: absolute; left: 36px; top: 160px; }
  .person-name { font-size: 28px; font-weight: 700; color: var(--navy); }
  .person-title { font-size: 17px; color: var(--muted); margin-top: 2px; }
  .rule-main { position: absolute; left: 36px; top: 240px; width: 440px; border-top: 1.5px solid var(--rule); }
  .contact { position: absolute; left: 36px; top: 252px; font-size: 18px; color: var(--ink); }
  .contact li { list-style: none; display: flex; align-items: center; gap: 10px; margin-bottom: 6px; }
  .contact svg { width: 16px; height: 16px; fill: var(--navy); }
  .rule-address { position: absolute; right: 40px; top: 300px; width: 240px; border-top: 1.5px solid var(--rule); }
  .address { position: absolute; right: 40px; top: 312px; text-align: right; font-size: 18px; color: var(--ink); line-height: 1.35; }
</style>
</head>
<body>
<main class="sheet">
  <section class="card card-back">
    <div class="siren siren-column" role="img" aria-label="Photo of a stacked column outdoor siren"></div>
    <div class="siren siren-horn" role="img" aria-label="Photo of a multi-horn outdoor siren unit"></div>
    <div class="back-copy">
      <p class="back-title">Outdoor sirens</p>
      <p class="back-lead">Notify people of severe dangers such as</p>
      <p class="back-list">Tornados • Severe thunderstorms • Flooding • Hurricanes • Tsunamis</p>
      <p class="back-lead">Oil and gas refining industries to warn of</p>
      <p class="back-list">Chemical releases • Fires • Lightning alerts</p>
    </div>
  </section>

  <section class="card card-front">
    <div class="brand">
      <div class="brand-line-1">Harborline</div>
      <div class="brand-line-2">Signal Systems</div>
    </div>
    <div class="person">
      <p class="person-name">Owen Trask</p>
      <p class="person-title">President</p>
    </div>
    <div class="rule-main"></div>
    <ul class="contact">
      <li>
        <svg viewBox="0 0 24 24" aria-hidden="true"><path d="M6.6 10.8a15.1 15.1 0 0 0 6.6 6.6l2.2-2.2a1 1 0 0 1 1-.25 11.4 11.4 0 0 0 3.6.57 1 1 0 0 1 1 1V20a1 1 0 0 1-1 1A17 17 0 0 1 3 4a1 1 0 0 1 1-1h3.5a1 1 0 0 1 1 1c0 1.25.2 2.46.57 3.6a1 1 0 0 1-.25 1z"/></svg>
        (662) 555-0148
      </li>
      <li>
        <svg viewBox="0 0 24 24" aria-hidden="true"><path d="M2 5h20v14H2z M2 5l10 8 10-8" /></svg>
        name@harborlinesignal.com
      </li>
    </ul>
    <div class="rule-address"></div>
    <p class="address">412 Mill Creek Road<br>Amory, MS 38821</p>
  </section>
</main>
</body>
</html>
```